Business Card Design for Small Electrical Contractor

I need to update my business card into something a little more modern. We are a small electrical contracting company. We service domestic and commercial places around Sydney. We have 2 logo designs at the moment. I have uploaded both and 2 different sizes to work with.

Industry/Entity Type

Business

Contact Information for Business Card

Leo Hartigan
8/21-23 Birch Rd, Kelsworth 2087
t - (02) 9381 4720
m - 0427 815 903
E - info@hartiganelx.com.au
W - hartiganelx.com.au
ABN: 42 907 551 316

Font styles to use
Sans Serif

Requirements
Must have
• I would also like to see the below fit on somewhere aswell
• - Licensed Electrician
• - Level 2 (Cat 1 & 4)
• - Domestic
• - Commercial
• - Repairs and Installations
• - Data
Nice to have
• Try and keep similar colours as logo
Should not have
• No lightning bolts or light globes. Smart and professional please.

```html
<!DOCTYPE html>
<html lang="en">
<head>
<meta charset="utf-8">
<title>Hartigan Electrical – Business Card</title>
<link href="https://fonts.googleapis.com/css2?family=Open+Sans:wght@400;600&display=swap" rel="stylesheet">
<style>
  :root {
    --backdrop: #8a8a8a;
    --card-white: #ffffff;
    --card-black: #050708;
    --brand-teal: #17383a;
    --brand-orange: #f39323;
    --ink: #222222;
    --muted-ink: #555555;
    --paper-text: #ffffff;
  }
  * { margin: 0; padding: 0; box-sizing: border-box; }
  html, body {
    width: 1200px; height: 1200px; overflow: hidden;
    background: var(--backdrop);
    font-family: "Open Sans", Arial, sans-serif;
  }
  .canvas { position: relative; width: 1200px; height: 1200px; }
  .card {
    position: absolute; left: 318px; width: 611px; height: 346px;
    overflow: hidden;
  }
  .card--front { top: 236px; background: var(--card-white); color: var(--ink); }
  .card--back { top: 634px; background: var(--card-black); color: var(--paper-text); }

  .brand {
    position: absolute; display: flex; align-items: center; gap: 12px;
    font-weight: 600; font-size: 31px; line-height: 40px; letter-spacing: 0.2px; white-space: nowrap;
  }
  .brand__mark { width: 14px; height: 14px; background: var(--brand-orange); flex: none; }
  .card--front .brand { left: 47px; top: 60px; color: var(--brand-teal); }
  .card--back .brand { left: 0; right: 0; top: 130px; justify-content: center; color: var(--paper-text); }

  .address { position: absolute; left: 40px; top: 193px; font-size: 14.5px; line-height: 20px; white-space: nowrap; }
  .contact-list { position: absolute; left: 39px; top: 227px; list-style: none; }
  .contact-list li {
    display: flex; align-items: center; height: 20.4px; font-size: 15px; white-space: nowrap;
  }
  .contact-list svg { width: 16px; height: 16px; margin-right: 11px; flex: none; }

  .person { position: absolute; right: 27px; top: 184px; text-align: right; white-space: nowrap; }
  .person__name { font-size: 22px; line-height: 28px; }
  .person__abn { font-size: 15px; line-height: 22px; }
  .person__abn-label { color: var(--brand-orange); }
  .accent-bar {
    position: absolute; right: 0; top: 190px; width: 12px; height: 38px;
    background: var(--brand-orange);
  }

  .services {
    position: absolute; right: 27px; top: 246px; text-align: right;
    list-style: none; font-size: 11px; line-height: 16px; color: var(--muted-ink); white-space: nowrap;
  }
  .services__lead { font-weight: 600; color: var(--brand-teal); }

  .back-web {
    position: absolute; left: 0; right: 0; top: 308px; text-align: center;
    font-size: 14.5px; line-height: 20px;
  }
</style>
</head>
<body>
<div class="canvas">
  <section class="card card--front">
    <div class="brand"><span class="brand__mark"></span>Hartigan Electrical</div>

    <p class="address">8/21-23 Birch Rd, Kelsworth 2087</p>
    <ul class="contact-list">
      <li>
        <svg viewBox="0 0 16 16" fill="var(--brand-orange)"><path d="M1 6c0-2 3-3 7-3s7 1 7 3v1.5h-3.5V6H4.5v1.5H1z"/><path d="M3 9l2-2h6l2 2v4H3z"/><circle cx="8" cy="10.5" r="1.6" fill="#fff"/></svg>
        (02) 9381 4720
      </li>
      <li>
        <svg viewBox="0 0 16 16" fill="none" stroke="var(--brand-orange)" stroke-width="1.6"><rect x="4" y="1.5" width="8" height="13" rx="1.5"/><line x1="7" y1="12" x2="9" y2="12"/></svg>
        0427 815 903
      </li>
      <li>
        <svg viewBox="0 0 16 16"><rect x="1" y="3.5" width="14" height="9" fill="var(--brand-orange)"/><path d="M1 3.5l7 5 7-5" fill="none" stroke="#fff" stroke-width="1.2"/></svg>
        info@hartiganelx.com.au
      </li>
      <li>
        <svg viewBox="0 0 16 16" fill="none" stroke="var(--brand-orange)" stroke-width="1.2"><circle cx="8" cy="8" r="6.5"/><ellipse cx="8" cy="8" rx="3" ry="6.5"/><line x1="1.5" y1="8" x2="14.5" y2="8"/><line x1="2.5" y1="4.8" x2="13.5" y2="4.8"/><line x1="2.5" y1="11.2" x2="13.5" y2="11.2"/></svg>
        hartiganelx.com.au
      </li>
    </ul>

    <div class="person">
      <p class="person__name">Leo Hartigan</p>
      <p class="person__abn"><span class="person__abn-label">ABN:</span> 42 907 551 316</p>
    </div>
    <div class="accent-bar"></div>

    <ul class="services">
      <li class="services__lead">Licensed Electrician · Level 2 (Cat 1 &amp; 4)</li>
      <li>Domestic · Commercial · Data</li>
      <li>Repairs and Installations</li>
    </ul>
  </section>

  <section class="card card--back">
    <div class="brand"><span class="brand__mark"></span>Hartigan Electrical</div>
    <p class="back-web">hartiganelx.com.au</p>
  </section>
</div>
</body>
</html>
```